2013 Golf Outing Flyer

Our charitable organization was created in honor of my daughter who died at age 16. Our annual fundraiser is a golf tournament. I am not a creative person so I'd like someone to design a printable flyer that grabs people's attention but is not too busy while incorportating our organization's logo with the basic information.

Event details:
3rd Annual Marisol Quinn Dorsey Memorial Golf Tournament
4 person scramble

Saturday October 5th, 2013
Fernhollow Golf Club, Auburn, IL
9:30 Registration
Shotgun start at noon
To Register go online to www.marisolqdorseygolf.teeupsignups.example or email
marisoldorseyscholarship@mailbox.example

Scholarships to Cedar Ridge High School seniors are made possible by our orgnization through this fundraiser.
Updates

Target Market(s)

golfers and businesses willing to sponsor event

Industry/Entity Type

School

Requirements
Must have
• single page-easy to print
includes non profit organization logo which I attached (think I did)
Specific information about the tournament- date and location and registration info
Nice to have
• company logo and the golf outing logo but if both are too much, then just the golf logo and the organization name can be at the bottom

```html
<!DOCTYPE html>
<html lang="en">
<head>
<meta charset="utf-8">
<title>3rd Annual Marisol Quinn Dorsey Memorial Golf Tournament</title>
<link href="https://fonts.googleapis.com/css2?family=Source+Sans+3:wght@400;600&display=swap" rel="stylesheet">
<style>
  :root {
    --bg: #f3e4ec;
    --tile-light: #f6ebf1;
    --tile-mid: #e9d0dd;
    --tile-deep: #dfbfcf;
    --rule: #8e2a8c;
    --purple: #6b2f95;
    --navy: #2c3a8e;
    --brown: #5b3a1c;
    --red: #c1272d;
    --blue: #1f6db4;
  }
  html, body { margin: 0; padding: 0; overflow: hidden; }
  body { width: 900px; height: 1200px; }
  .flyer {
    position: relative;
    width: 900px;
    height: 1200px;
    overflow: hidden;
    background: var(--bg);
    font-family: "Source Sans 3", "Myriad Pro", sans-serif;
  }
  .tile { position: absolute; }
  .tile-a { left: 0; top: 0; width: 470px; height: 475px; background: linear-gradient(90deg, var(--tile-light), var(--tile-deep)); }
  .tile-b { left: 255px; top: 0; width: 345px; height: 310px; background: linear-gradient(90deg, var(--tile-light), var(--tile-mid)); }
  .tile-c { left: 600px; top: 0; width: 300px; height: 230px; background: linear-gradient(90deg, var(--tile-mid), var(--tile-deep)); }
  .tile-d { left: 595px; top: 230px; width: 305px; height: 410px; background: linear-gradient(90deg, var(--tile-light), var(--tile-mid)); }
  .tile-e { left: 0; top: 475px; width: 430px; height: 400px; background: linear-gradient(90deg, var(--tile-light), var(--tile-mid)); }
  .tile-f { left: 430px; top: 380px; width: 300px; height: 520px; background: linear-gradient(90deg, var(--tile-mid), var(--tile-light)); }
  .tile-g { left: 730px; top: 640px; width: 170px; height: 260px; background: linear-gradient(90deg, var(--tile-light), var(--tile-deep)); }
  .tile-h { left: 0; top: 875px; width: 600px; height: 325px; background: linear-gradient(90deg, var(--tile-light), var(--tile-mid)); }
  .tile-i { left: 600px; top: 900px; width: 300px; height: 300px; background: linear-gradient(90deg, var(--tile-mid), var(--tile-light)); }
  .rules { position: absolute; left: 0; top: 0; }
  .org-name {
    position: absolute;
    left: 70px;
    top: 140px;
    width: 250px;
    margin: 0;
    text-align: center;
    color: var(--purple);
    font-weight: 600;
    font-size: 28px;
    line-height: 1.15;
  }
  .headline { position: absolute; left: 390px; top: 78px; margin: 0; font-weight: 400; }
  .headline span { display: block; }
  .headline .edition { color: var(--purple); font-size: 35px; line-height: 48px; }
  .headline .title { color: var(--navy); font-size: 37px; line-height: 48px; }
  .format { position: absolute; left: 390px; top: 240px; margin: 0; color: var(--brown); font-size: 36px; font-weight: 400; }
  .details { position: absolute; left: 237px; top: 474px; margin: 0; font-size: 31px; line-height: 48px; }
  .details .heading { color: var(--red); display: block; }
  .details .row { display: flex; }
  .details dt { color: var(--red); width: 122px; margin: 0; }
  .details dd { color: var(--blue); margin: 0; }
  .details .indent { padding-left: 128px; color: var(--blue); }
  .register { position: absolute; left: 160px; top: 936px; margin: 0; font-size: 31px; line-height: 44px; }
  .register .label { color: var(--red); display: block; }
  .register .link { color: var(--blue); display: block; }
  .note { position: absolute; left: 160px; top: 1130px; margin: 0; color: var(--red); font-size: 19px; line-height: 25px; }
</style>
</head>
<body>
<main class="flyer">
  <div class="tile tile-a"></div>
  <div class="tile tile-b"></div>
  <div class="tile tile-c"></div>
  <div class="tile tile-d"></div>
  <div class="tile tile-e"></div>
  <div class="tile tile-f"></div>
  <div class="tile tile-g"></div>
  <div class="tile tile-h"></div>
  <div class="tile tile-i"></div>

  <svg class="rules" width="900" height="1200" viewBox="0 0 900 1200" aria-hidden="true">
    <polygon points="248,307 900,302 900,310 248,308" fill="var(--rule)"/>
    <polygon points="0,421 670,425 670,426 0,430" fill="var(--rule)"/>
    <polygon points="0,775 670,779 670,780 0,784" fill="var(--rule)"/>
    <polygon points="248,907 900,902 900,910 248,908" fill="var(--rule)"/>
  </svg>

  <p class="org-name">MQD<br>Memorial Golf Outing</p>

  <h1 class="headline">
    <span class="edition">3rd Annual</span>
    <span class="title">Marisol Quinn Dorsey</span>
    <span class="title">Memorial Golf Tournament</span>
  </h1>
  <p class="format">4 person scramble</p>

  <dl class="details">
    <span class="heading">Event&nbsp; Details</span>
    <div class="row"><dt>place :</dt><dd>Fernhollow Golf Club, Auburn, IL</dd></div>
    <div class="row"><dt>Date&nbsp; :</dt><dd>Saturday October 5th, 2013</dd></div>
    <div class="row"><dt>Time&nbsp; :</dt><dd>&nbsp;9:30&nbsp;&nbsp; Registration</dd></div>
    <div class="indent">Shotgun start at noon</div>
  </dl>

  <p class="register">
    <span class="label">Register online at</span>
    <span class="link">www.marisolqdorseygolf.teeupsignups.example</span>
    <span class="label">or email at</span>
    <span class="link">marisoldorseyscholarship@mailbox.example</span>
  </p>

  <p class="note">Scholarships to Cedar Ridge High School seniors are made possible<br>by our orgnization through this fundraise</p>
</main>
</body>
</html>
```